We need an Infographic illustration ‘How it works’ section for our car hire business

Need the infographic design to match the look and feel of our website, the images already in use etc.. The 3 steps to the infographic diagram are:

(A) Get fast approval for a hire car by phone or online.

(B) We deliver a hire car to your location.

(C) When your own car has been repaired, we collect our hire car and finalize paperwork on your behalf with the insurance company.

We do not need text for the infographic as a short paragraph will be added below each step by ourselves. Think it’s very important that the new image style works with the images we already have on our site!! Thank you for taking the time and please contact me with any questions.

Industry/Entity Type

Car Rental

Colors

Designer to choose colors to be used in the design.

Requirements
Must have
• NEEDS TO FIT WITH THE ATMOSPHERE and with the images we already have in use on our website.
Should not have
• Needs to fit with the colours and feel of our website as per attachment.

```html
<!DOCTYPE html>
<html lang="en">
<head>
<meta charset="utf-8">
<title>Zestline – How It Works</title>
<link rel="stylesheet" href="https://fonts.googleapis.com/css2?family=Exo+2:wght@400;500;600;700;800&family=Roboto:wght@400;500&display=swap">
<style>
  :root {
    --canvas: #bcbdd3;
    --header-dark: #16171b;
    --hero-grey: #6e6e6e;
    --black: #000000;
    --white: #ffffff;
    --yellow: #f7d708;
    --green: #8cc63f;
    --green-dark: #7ab530;
    --text-dark: #2b2b2b;
    --text-muted: #d9d9d9;
  }
  * { box-sizing: border-box; margin: 0; padding: 0; }
  html, body { width: 1200px; height: 1200px; overflow: hidden; }
  body { background: var(--canvas); font-family: "Exo 2", sans-serif; position: relative; }

  .page { position: absolute; left: 144px; top: 30px; width: 938px; height: 1054px; background: var(--white); overflow: hidden; }

  /* Header */
  .site-header { position: absolute; left: 0; top: 0; width: 938px; height: 103px; background: var(--header-dark); }
  .brand { position: absolute; left: 42px; top: 22px; display: flex; align-items: center; gap: 12px; }
  .brand-mark { width: 50px; height: 50px; background: var(--yellow); border-radius: 8px; }
  .brand-text { display: flex; flex-direction: column; }
  .brand-name { font-weight: 600; font-size: 44px; line-height: 40px; color: var(--white); letter-spacing: 0.5px; }
  .brand-tagline { font-weight: 600; font-size: 12px; letter-spacing: 3.6px; color: var(--white); margin-top: 3px; }
  .header-cta { position: absolute; right: 47px; top: 20px; display: flex; flex-direction: column; align-items: flex-end; }
  .header-question { font-family: "Roboto", sans-serif; font-size: 11px; color: var(--text-muted); margin-right: 10px; }
  .call-button { margin-top: 14px; height: 29px; width: 195px; background: var(--yellow); border-radius: 15px; display: flex; align-items: center; justify-content: center; gap: 6px; font-family: "Roboto", sans-serif; font-weight: 500; font-size: 16px; color: var(--black); }
  .call-button svg { width: 14px; height: 14px; }

  /* Hero */
  .hero { position: absolute; left: 0; top: 103px; width: 938px; height: 375px; background: var(--hero-grey); }
  .quote-form { position: absolute; left: 678px; top: 210px; width: 220px; height: 296px; }

  /* How it works band */
  .intro-band { position: absolute; left: 0; top: 527px; width: 938px; height: 192px; background: var(--black); padding: 50px 0 0 35px; }
  .intro-title { font-weight: 700; font-size: 35px; line-height: 40px; color: var(--yellow); }
  .intro-lead { margin-top: 14px; font-weight: 600; font-size: 17px; line-height: 20px; color: var(--white); width: 620px; }

  /* Steps */
  .steps { position: absolute; left: 0; top: 719px; width: 938px; height: 335px; }
  .steps-path { position: absolute; left: 0; top: 0; }
  .step-number { position: absolute; width: 56px; height: 56px; background: var(--yellow); color: var(--white); font-weight: 700; font-size: 40px; line-height: 56px; text-align: center; }
  .step-art { position: absolute; border-radius: 10px; }
  .step-copy { position: absolute; width: 240px; text-align: center; }
  .step-title { font-weight: 600; font-size: 15px; line-height: 16px; color: var(--green); text-transform: uppercase; }
  .step-rule { width: 66px; height: 2px; background: var(--yellow); margin: 5px auto 6px; }
  .step-text { font-family: "Roboto", sans-serif; font-size: 9.5px; line-height: 11.5px; color: var(--text-dark); }
</style>
</head>
<body>
  <main class="page">
    <header class="site-header">
      <div class="brand">
        <div class="brand-mark"></div>
        <div class="brand-text">
          <span class="brand-name">Zestline</span>
          <span class="brand-tagline">ACCIDENT SOLUTIONS</span>
        </div>
      </div>
      <div class="header-cta">
        <span class="header-question">Not at-fault in a traffic accident?</span>
        <div class="call-button">
          <svg viewBox="0 0 24 24" aria-hidden="true"><path fill="#000" d="M6.6 10.8a15.1 15.1 0 0 0 6.6 6.6l2.2-2.2c.3-.3.7-.4 1-.2 1.1.4 2.3.6 3.6.6.6 0 1 .4 1 1V20c0 .6-.4 1-1 1A17 17 0 0 1 3 4c0-.6.4-1 1-1h3.5c.6 0 1 .4 1 1 0 1.3.2 2.5.6 3.6.1.3 0 .7-.2 1z"/></svg>
          <span>Free 1800 555 019</span>
        </div>
      </div>
    </header>

    <section class="hero"></section>

    <svg class="quote-form" viewBox="0 0 220 296" aria-label="Quote request form">
      <path d="M0 30 Q0 0 30 0 H190 Q220 0 220 30 V44 H0 Z" fill="#ffffff"/>
      <path d="M0 44 H220 V268 L110 296 L0 268 Z" fill="#8cc63f"/>
      <g fill="#f7d708" stroke="#e0a800" stroke-width="0.8">
        <path transform="translate(30 24)" d="M0-15 4.4-5 15.2-4.6 6.7 2.2 9.4 12.6 0 6.6-9.4 12.6-6.7 2.2-15.2-4.6-4.4-5Z"/>
        <path transform="translate(70 24)" d="M0-15 4.4-5 15.2-4.6 6.7 2.2 9.4 12.6 0 6.6-9.4 12.6-6.7 2.2-15.2-4.6-4.4-5Z"/>
        <path transform="translate(110 24)" d="M0-15 4.4-5 15.2-4.6 6.7 2.2 9.4 12.6 0 6.6-9.4 12.6-6.7 2.2-15.2-4.6-4.4-5Z"/>
        <path transform="translate(150 24)" d="M0-15 4.4-5 15.2-4.6 6.7 2.2 9.4 12.6 0 6.6-9.4 12.6-6.7 2.2-15.2-4.6-4.4-5Z"/>
        <path transform="translate(190 24)" d="M0-15 4.4-5 15.2-4.6 6.7 2.2 9.4 12.6 0 6.6-9.4 12.6-6.7 2.2-15.2-4.6-4.4-5Z"/>
      </g>
      <rect x="12" y="68" width="195" height="24" fill="#ffffff"/>
      <rect x="12" y="117" width="195" height="24" fill="#ffffff"/>
      <rect x="12" y="167" width="195" height="24" fill="#ffffff"/>
      <rect x="11" y="214" width="198" height="25" rx="12.5" fill="#f7d708"/>
    </svg>

    <section class="intro-band">
      <h2 class="intro-title">How It Works</h2>
      <p class="intro-lead">There is no catch. You just need to provide us with the relevant details and we will take care of the rest!</p>
    </section>

    <section class="steps">
      <svg class="steps-path" width="938" height="335" viewBox="0 0 938 335" aria-hidden="true">
        <defs>
          <linearGradient id="pathGradient" x1="0" y1="0" x2="938" y2="0" gradientUnits="userSpaceOnUse">
            <stop offset="0" stop-color="#f7d708"/>
            <stop offset="0.28" stop-color="#f7d708"/>
            <stop offset="0.40" stop-color="#8cc63f"/>
            <stop offset="0.55" stop-color="#f7d708"/>
            <stop offset="0.75" stop-color="#f7d708"/>
            <stop offset="0.92" stop-color="#8cc63f"/>
            <stop offset="1" stop-color="#f7d708"/>
          </linearGradient>
        </defs>
        <path d="M0 227 H60 Q88 227 88 199 V71 Q88 43 116 43 H316 Q344 43 344 71 V199 Q344 227 372 227 H568 Q596 227 596 199 V71 Q596 43 624 43 H838 Q866 43 866 71 V199 Q866 227 894 227 H938"
              fill="none" stroke="url(#pathGradient)" stroke-width="17"/>
      </svg>

      <div class="step-number" style="left:104px; top:59px;">1</div>
      <div class="step-number" style="left:525px; top:154px;">2</div>
      <div class="step-number" style="left:614px; top:59px;">3</div>

      <div class="step-art" role="img" aria-label="Illustration of a computer and tablet with an approval tick"
           style="left:164px; top:83px; width:144px; height:155px; background:radial-gradient(circle at 45% 60%, #1cc7b1 0 40%, #e9f6f3 41%);"></div>
      <div class="step-art" role="img" aria-label="Illustration of a hand offering a hire car, motorbike and key"
           style="left:372px; top:48px; width:152px; height:156px; background:linear-gradient(160deg, #eef6e2, #cfe9a8 60%, #f7d9c2);"></div>
      <div class="step-art" role="img" aria-label="Illustration of insurance paperwork with a car and shield"
           style="left:688px; top:83px; width:142px; height:136px; background:linear-gradient(160deg, #dbe9f7, #b9d3ef 70%, #f3e8a8);"></div>

      <div class="step-copy" style="left:97px; top:255px;">
        <h3 class="step-title">Eligibility Check</h3>
        <div class="step-rule"></div>
        <p class="step-text">Lorem ipsum dolor sit amet, consectetur adipiscing elit. Sed volutpat pretium pharetra. Maecenas porta diam justo, vitae hendrerit nisi commodo et.</p>
      </div>
      <div class="step-copy" style="left:354px; top:255px;">
        <h3 class="step-title">Hired-Vehicle Delivery (ASAP)</h3>
        <div class="step-rule"></div>
        <p class="step-text">Lorem ipsum dolor sit amet, consectetur adipiscing elit. Sed volutpat pretium pharetra. Maecenas porta diam justo, vitae hendrerit nisi commodo et.</p>
      </div>
      <div class="step-copy" style="left:618px; top:239px;">
        <h3 class="step-title">Vehicle Collection &amp;<br>Insurance Paperwork</h3>
        <div class="step-rule"></div>
        <p class="step-text">Lorem ipsum dolor sit amet, consectetur adipiscing elit. Sed volutpat pretium pharetra. Maecenas porta diam justo, vitae hendrerit nisi commodo et.</p>
      </div>
    </section>
  </main>
</body>
</html>
```